Create look and feel for existing Web Page

Update Web Page

We have a website at http://www.getmirvo.com/index-web.html. It is a single page html site, with a custom signup form. We also have a zen desk plugin at the bottom of the page. We'd like to redesign the look and feel of the entire site. We sell software to eye doctors. Also called optometrists, our software tool makes it easy for doctors to manage patients, bill, and document patient encounters. I have included our logos below.

We are looking for a new design preferably in HTML 5, CSS etc. The fields on the form on this page: http://www.getmirvo.com/index-web.html

You can get screen shots of our software application at this site: http://staging.getmirvo.com
username: test@sampledomain-mirvo.com
password: password

```html
<!DOCTYPE html>
<html lang="en">
<head>
<meta charset="utf-8">
<title>mirvo – Practice Operating System</title>
<link href="https://fonts.googleapis.com/css2?family=League+Spartan:wght@500;600;700&family=Nunito:wght@400;600;700&family=Oswald:wght@500&display=swap" rel="stylesheet">
<style>
:root{
  --orange:#f7841c;
  --orange-deep:#f06f0c;
  --orange-soft:#fcae5c;
  --ink:#2f3542;
  --text:#4a4f5a;
  --muted:#6a6f78;
  --grey-btn:#6d6d6d;
  --cream:#fff7f0;
  --panel:#f7f8fa;
  --line:#e9ebee;
  --footer:#2c2c2f;
  --white:#ffffff;
}
*{box-sizing:border-box;margin:0;padding:0}
html,body{width:1200px;height:3580px;overflow:hidden;background:var(--white)}
body{position:relative;font-family:"Nunito",sans-serif;color:var(--text)}
.abs{position:absolute}
.heading{font-family:"League Spartan",sans-serif;font-weight:600;color:var(--ink)}
.center{text-align:center;left:0;width:1200px}

/* header */
.site-header{position:absolute;left:0;top:0;width:1200px;height:100px;background:var(--white)}
.brand{position:absolute;left:139px;top:18px;font-family:"Nunito",sans-serif;font-weight:600;font-size:54px;color:#6a6a6a;letter-spacing:1px;line-height:1}
.nav a{position:absolute;top:39px;font-size:14px;font-weight:600;color:#333;text-decoration:none;letter-spacing:.5px}
.nav a.active{color:var(--orange)}
.btn{position:absolute;display:flex;align-items:center;justify-content:center;border-radius:22px;color:var(--white);font-weight:700;font-size:14px;text-decoration:none;letter-spacing:.4px}
.btn-orange{background:var(--orange)}
.btn-grey{background:var(--grey-btn)}

/* hero */
.hero-bg{position:absolute;left:0;top:100px;width:1200px;height:580px}
.hero-title{top:150px;font-size:42px;line-height:52px;color:var(--white);font-weight:700}
.hero-copy{top:266px;font-size:15px;line-height:25px;color:#fff4ea}
.laptop-screen{position:absolute;left:342px;top:445px;width:516px;height:328px;border-radius:2px;background:linear-gradient(90deg,#34373d 0 107px,#eef0f3 107px)}

/* features */
.eyebrow{font-size:18px;color:var(--orange)}
.section-title{font-size:30px}
.lead{font-size:15.5px;line-height:28px;color:#3f434b}
.feature{position:absolute;width:314px;text-align:center}
.feature .icon{width:70px;height:70px;border-radius:18px;margin:0 auto;display:flex;align-items:center;justify-content:center}
.feature h3{font-family:"Nunito",sans-serif;font-weight:700;font-size:19px;color:#333;margin-top:18px}
.feature p{font-size:13px;line-height:21px;color:#4f535b;margin:8px auto 0;width:270px}
.divider-v{position:absolute;width:1px;background:var(--line)}
.divider-h{position:absolute;height:1px;background:var(--line)}

/* pricing */
.pricing-bg{position:absolute;left:0;top:1842px;width:1200px;height:760px}
.price-card{position:absolute;top:1997px;width:438px;height:310px;background:var(--white);box-shadow:0 4px 18px rgba(0,0,0,.08);overflow:hidden;text-align:center}
.price-card .corner{position:absolute;left:-90px;top:-90px;width:180px;height:180px;border-radius:50%;background:var(--orange)}
.price-card .amount{position:absolute;left:108px;top:20px;display:flex;align-items:baseline;color:var(--ink);font-family:"Oswald",sans-serif}
.amount .cur{font-size:38px;margin-right:4px}
.amount .num{font-size:64px;line-height:1}
.amount .per{font-size:26px;margin-left:4px}
.amount .loc{font-family:"Nunito",sans-serif;font-size:14px;margin-left:12px;color:#444}
.price-card h3{position:absolute;top:118px;left:0;width:100%;font-family:"League Spartan",sans-serif;font-weight:600;font-size:20px;color:var(--ink)}
.price-card p{position:absolute;top:150px;left:0;width:100%;font-size:15px;line-height:28px;color:#3f434b}

/* about */
.about-panel{position:absolute;left:493px;top:2585px;width:565px;height:452px;background:var(--panel)}
.about-photo{position:absolute;left:140px;top:2633px;width:410px;height:357px;background:linear-gradient(160deg,#8a8f7a,#b9a48b 45%,#e2c3a7 70%,#3c3a38)}
.about-brand{left:603px;top:2632px;font-size:32px;font-weight:600;color:var(--orange);letter-spacing:1px}
.about-h{left:605px;font-size:26px;line-height:35px}
.checks{left:605px;top:2853px;font-size:17px;color:var(--orange);display:flex;gap:28px}
.checks span{display:flex;align-items:center;gap:5px}

/* waitlist */
.field{position:absolute;width:290px;height:42px;border:1px solid #d9dbe0;border-radius:3px;background:var(--white);display:flex;align-items:center;font-size:13px;color:#555}
.field .ico{width:38px;height:100%;display:flex;align-items:center;justify-content:center;border-right:1px solid #e2e4e8;margin-right:14px}
.help{position:absolute;left:1016px;top:3430px;width:76px;height:76px;border-radius:50%;background:#f1f2f4;box-shadow:0 2px 8px rgba(0,0,0,.08);text-align:center;font-size:14px;font-weight:700;color:#333}

/* footer */
.site-footer{position:absolute;left:0;top:3524px;width:1200px;height:56px;background:var(--footer)}
.site-footer p{position:absolute;left:142px;top:19px;font-size:12.5px;color:#ddd}
.social{position:absolute;top:13px;width:30px;height:30px;border-radius:50%}
</style>
</head>
<body>

<header class="site-header">
  <div class="brand">mirvo</div>
  <nav class="nav">
    <a class="active" href="#" style="left:616px">HOME</a>
    <a href="#" style="left:709px">PRODUCTS</a>
    <a href="#" style="left:842px">PRICING</a>
  </nav>
  <a class="btn btn-orange" href="#" style="left:944px;top:26px;width:114px;height:42px">SIGN UP</a>
</header>

<!-- hero -->
<svg class="hero-bg" viewBox="0 0 1200 580" role="img" aria-label="Optometrist examining a patient at an eye test device, tinted orange">
  <defs>
    <linearGradient id="heroGrad" x1="0" y1="0" x2="1" y2="1">
      <stop offset="0" stop-color="#f6892a"/>
      <stop offset=".55" stop-color="#f79a45"/>
      <stop offset="1" stop-color="#f5b37a"/>
    </linearGradient>
  </defs>
  <path d="M0 0H1200V570C1080 545 960 560 840 575 720 590 600 560 480 552 360 545 240 565 120 562 70 560 30 555 0 560Z" fill="url(#heroGrad)"/>
  <circle cx="180" cy="140" r="100" fill="#f57f15" opacity=".55"/>
  <circle cx="1200" cy="140" r="140" fill="#f57f15" opacity=".55"/>
  <circle cx="275" cy="390" r="45" fill="#f57f15" opacity=".7"/>
</svg>

<h1 class="abs center heading hero-title">Lease Practices:<br>Choose How You Spend Your Time</h1>
<p class="abs center hero-copy">Mirvo is your office operating system. Automate your painful tasks, keep track of your books, and live a little.<br>Start with a tool that eliminates paper charts and add more products as you grow.</p>
<a class="btn btn-grey" href="#" style="left:443px;top:331px;width:315px;height:38px;font-size:13px">STOP WASTING MONEY ON PAPER TODAY</a>

<svg class="abs" style="left:260px;top:415px" width="680" height="440" viewBox="0 0 680 440">
  <ellipse cx="340" cy="410" rx="300" ry="22" fill="#000" opacity=".05"/>
  <rect x="58" y="10" width="565" height="378" rx="14" fill="#fff" stroke="#e4e6ea"/>
  <rect x="8" y="382" width="665" height="10" rx="5" fill="#eceef1"/>
  <rect x="280" y="382" width="120" height="4" rx="2" fill="#d6d8dc"/>
</svg>
<div class="laptop-screen" role="img" aria-label="Screenshot of the scheduling screen of the practice software"></div>

<!-- features -->
<p class="abs center eyebrow" style="top:918px">Join the Cool Club</p>
<h2 class="abs center heading section-title" style="top:950px">AI to Automate Optometry Office Tasks</h2>
<p class="abs center lead" style="top:994px">Mirvo uses AI, automation, robots, and other cool technology to streamline office work<br>so you can do things you love</p>

<div class="divider-v" style="left:442px;top:1080px;height:685px"></div>
<div class="divider-v" style="left:756px;top:1080px;height:685px"></div>
<div class="divider-h" style="left:140px;top:1320px;width:918px"></div>
<div class="divider-h" style="left:140px;top:1566px;width:918px"></div>

<div class="feature" style="left:128px;top:1088px">
  <div class="icon" style="background:#eceded"><svg width="40" height="40" viewBox="0 0 40 40" fill="none" stroke="#555" stroke-width="1.6"><rect x="8" y="6" width="16" height="28" rx="2"/><rect x="18" y="14" width="14" height="20" rx="2"/><line x1="13" y1="30" x2="17" y2="30"/></svg></div>
  <h3>Schedule</h3>
  <p>Meet your patients where they are, 24 hours 7 days a week with the online scheduler.</p>
</div>
<div class="feature" style="left:442px;top:1088px">
  <div class="icon" style="background:#eaf3fd"><svg width="40" height="40" viewBox="0 0 40 40" fill="none" stroke="#3b8de0" stroke-width="1.6"><circle cx="24" cy="14" r="6"/><circle cx="24" cy="14" r="2"/><circle cx="14" cy="26" r="6"/><circle cx="14" cy="26" r="2"/></svg></div>
  <h3>Intake</h3>
  <p>Never print out another paper form. Your patients are now able to fill out and sign forms online.</p>
</div>
<div class="feature" style="left:756px;top:1088px">
  <div class="icon" style="background:#f1edfb"><svg width="40" height="40" viewBox="0 0 40 40" fill="none" stroke="#7b5fd0" stroke-width="1.6"><path d="M8 30 28 10l4 4-20 20H8z"/><path d="M10 10l20 20"/></svg></div>
  <h3>Chart</h3>
  <p>The HIPAA compliant charting tool allows you to eliminate paper and folders, plus allows your practice to use a customizable calendar system for bookings.</p>
</div>

<div class="feature" style="left:128px;top:1354px">
  <div class="icon" style="background:#fdf6dc"><svg width="40" height="40" viewBox="0 0 40 40" fill="none" stroke="#e8b620" stroke-width="1.6"><path d="M20 8 34 15 20 22 6 15z"/><path d="M6 20l14 7 14-7"/><path d="M6 25l14 7 14-7"/></svg></div>
  <h3>Bill</h3>
  <p>Don't waste your precious time or pay someone to bill insurance, let a bot do it for you.</p>
</div>
<div class="feature" style="left:442px;top:1354px">
  <div class="icon" style="background:#e6f7ea"><svg width="40" height="40" viewBox="0 0 40 40" fill="none" stroke="#3cb35a" stroke-width="1.6"><path d="M16 12l4-4 4 4"/><path d="M10 28l-2-5 5-1"/><path d="M30 28h-6l2-4"/></svg></div>
  <h3>Eligible</h3>
  <p>Don't call or login into every insurance website to get patient eligibility and copays. Our bots do that too.</p>
</div>
<div class="feature" style="left:756px;top:1354px">
  <div class="icon" style="background:#fdecef"><svg width="40" height="40" viewBox="0 0 40 40" fill="none" stroke="#e84a64" stroke-width="1.8"><path d="M20 32S7 24 7 15a6.5 6.5 0 0 1 13-2 6.5 6.5 0 0 1 13 2c0 9-13 17-13 17z"/></svg></div>
  <h3>Review</h3>
  <p>Grow your patient base and improve your online search results with the review solution.</p>
</div>

<div class="feature" style="left:128px;top:1600px">
  <div class="icon" style="background:#e6f7ea"><svg width="40" height="40" viewBox="0 0 40 40" fill="none" stroke="#3cb35a" stroke-width="1.6"><rect x="6" y="14" width="28" height="20" rx="1"/><path d="M6 14l14 11 14-11"/><rect x="12" y="6" width="16" height="14"/></svg></div>
  <h3>Post</h3>
  <p>Stop printing postcards and licking stamps. Mirvo sends personalized postcards for you.</p>
</div>
<div class="feature" style="left:442px;top:1600px">
  <div class="icon" style="background:#f1edfb"><svg width="40" height="40" viewBox="0 0 40 40" fill="none" stroke="#7b5fd0" stroke-width="1.6"><path d="M14 12h16a4 4 0 0 1 4 4v6a4 4 0 0 1-4 4h-2v4l-5-4h-9a4 4 0 0 1-4-4v-6a4 4 0 0 1 4-4z"/><path d="M8 22a4 4 0 0 1-2-3v-5a4 4 0 0 1 4-4"/></svg></div>
  <h3>Remind</h3>
  <p>No need for phone call reminders, we send text and email reminders to your patients.</p>
</div>
<div class="feature" style="left:756px;top:1600px">
  <div class="icon" style="background:#fdf6dc"><svg width="40" height="40" viewBox="0 0 40 40" fill="none" stroke="#e8b620" stroke-width="1.8"><path d="M30 16A11 11 0 0 0 10 14"/><path d="M30 8v8h-8"/><path d="M10 24a11 11 0 0 0 20 2"/><path d="M10 32v-8h8"/></svg></div>
  <h3>Recall</h3>
  <p>Annual exams are important for the bottom line. Mirvo sends recalls via text and email.</p>
</div>

<!-- pricing -->
<svg class="pricing-bg" viewBox="0 0 1200 760">
  <path d="M0 0H1200V690C1100 640 990 665 860 700 720 740 560 720 400 700 250 682 120 690 0 735Z" fill="var(--cream)"/>
</svg>
<h2 class="abs center heading section-title" style="top:1920px">Our Pricing</h2>

<div class="price-card" style="left:140px">
  <div class="corner"></div>
  <svg class="abs" style="left:16px;top:20px" width="44" height="50" viewBox="0 0 44 50" fill="none" stroke="#fff" stroke-width="2"><rect x="4" y="4" width="30" height="40"/><path d="M10 14h12M10 20h10M10 26h8"/><circle cx="30" cy="20" r="7"/><path d="M27 20l2 2 4-4"/></svg>
  <div class="amount"><span class="cur">$</span><span class="num">20</span><span class="per">/mo</span><span class="loc">Per Location</span></div>
  <h3>Lease Management Software</h3>
  <p>HIPAA compliant tool to chart patient findings, book<br>appointments, and write prescriptions digitally.</p>
  <a class="btn btn-grey" href="#" style="left:163px;top:223px;width:113px;height:38px">BUY NOW</a>
</div>
<div class="price-card" style="left:621px">
  <div class="corner"></div>
  <svg class="abs" style="left:16px;top:16px" width="44" height="54" viewBox="0 0 44 54" fill="none" stroke="#fff" stroke-width="2"><rect x="4" y="4" width="28" height="38"/><path d="M10 14h14M10 20h12M10 26h10"/><circle cx="28" cy="44" r="6" fill="#fff"/></svg>
  <div class="amount"><span class="cur">$</span><span class="num">99</span><span class="per">/mo</span><span class="loc">Per Location</span></div>
  <h3>Add-ons for only $99 each per month</h3>
  <p>Choose any or all features including schedule,<br>intake, eligible, bill, review, remind, post, and recall.</p>
  <a class="btn btn-grey" href="#" style="left:163px;top:223px;width:113px;height:38px">BUY NOW</a>
</div>

<!-- about -->
<div class="about-panel"></div>
<div class="about-photo" role="img" aria-label="Three smiling young women hiking in the mountains"></div>
<div class="abs about-brand">mirvo</div>
<h2 class="abs heading about-h" style="top:2685px">What If Running Your Lease Is<br>As Simple As A Mirvo Patient?</h2>
<h2 class="abs heading about-h" style="top:2765px">Meet Mirvo,<br>The Practice Operating System</h2>
<div class="abs checks">
  <span><svg width="16" height="16" viewBox="0 0 16 16" fill="none" stroke="var(--orange)" stroke-width="1.8"><rect x="1.5" y="2.5" width="11" height="11" rx="1.5"/><path d="M4.5 8l3 3 7-8"/></svg>Simple</span>
  <span><svg width="16" height="16" viewBox="0 0 16 16" fill="none" stroke="var(--orange)" stroke-width="1.8"><rect x="1.5" y="2.5" width="11" height="11" rx="1.5"/><path d="M4.5 8l3 3 7-8"/></svg>Fully Automated</span>
  <span><svg width="16" height="16" viewBox="0 0 16 16" fill="none" stroke="var(--orange)" stroke-width="1.8"><rect x="1.5" y="2.5" width="11" height="11" rx="1.5"/><path d="M4.5 8l3 3 7-8"/></svg>Profitable</span>
</div>
<p class="abs heading" style="left:605px;top:2898px;font-size:19px;font-weight:500">Just You &amp; Mirvo Can Run Your Lease Practice</p>
<a class="btn btn-orange" href="#" style="left:603px;top:2947px;width:146px;height:38px;font-size:13px">JOIN THE CLUB</a>

<!-- waitlist -->
<p class="abs center eyebrow" style="top:3141px">Get on the waitlist</p>
<h2 class="abs center heading section-title" style="top:3170px">Start Using Mirvo Today</h2>
<p class="abs center lead" style="top:3214px;font-size:15px;line-height:25px">Become part of a club that wants to change the way we practice,<br>so we can have a life outside of the office.</p>

<div class="field" style="left:303px;top:3285px"><span class="ico"><svg width="12" height="12" viewBox="0 0 12 12" fill="var(--orange)"><circle cx="6" cy="3.5" r="3"/><path d="M0 12a6 5 0 0 1 12 0z"/></svg></span>Name</div>
<div class="field" style="left:607px;top:3285px"><span class="ico"><svg width="13" height="10" viewBox="0 0 13 10" fill="var(--orange)"><rect width="13" height="10" rx="1"/><path d="M0 1l6.5 5L13 1" stroke="#fff" fill="none"/></svg></span>Email</div>
<div class="field" style="left:303px;top:3342px"><span class="ico"><svg width="12" height="12" viewBox="0 0 12 12" fill="var(--orange)"><path d="M2 0l2.5 3-1.5 1.5a7 7 0 0 0 4.5 4.5L9 7.5 12 10l-1.5 2C5 12 0 7 0 1.5z"/></svg></span>Phone</div>
<div class="field" style="left:607px;top:3342px"><span class="ico"><svg width="11" height="13" viewBox="0 0 11 13" fill="var(--orange)"><rect width="11" height="13"/><g fill="#fff"><rect x="2" y="2" width="2" height="2"/><rect x="7" y="2" width="2" height="2"/><rect x="2" y="6" width="2" height="2"/><rect x="7" y="6" width="2" height="2"/><rect x="4" y="10" width="3" height="3"/></g></svg></span>Offece Name</div>

<a class="btn btn-orange" href="#" style="left:505px;top:3414px;width:190px;height:38px;font-size:13px">GET ON THE WAITLIST</a>

<div class="help">
  <svg style="margin-top:18px" width="14" height="14" viewBox="0 0 14 14"><circle cx="7" cy="7" r="7" fill="#333"/><text x="7" y="11" font-size="10" font-weight="700" fill="#fff" text-anchor="middle" font-family="Nunito,sans-serif">?</text></svg>
  <div>HELP</div>
</div>

<footer class="site-footer">
  <p>Copyright © 2020 <strong>mirvo</strong>. All Rights Reserved.</p>
  <span class="social" style="left:958px;background:#3b5aa8"></span>
  <span class="social" style="left:994px;background:#36a9e6"></span>
  <span class="social" style="left:1029px;background:#1878b4"></span>
</footer>

</body>
</html>
```